RMT Property - Business Cards

Looking for a business card & general letterhead, signage etc design for our new logo.

Colours:
000a20
0056a2
00b5ef
0088ce
68cef2

Fonts:
Poppins
Karla

Please keep look and feel of new brand - example in the zip package I sent.

```html
<!DOCTYPE html>
<html lang="en">
<head>
<meta charset="utf-8">
<title>RMT Property – Business Cards</title>
<link rel="stylesheet" href="https://fonts.googleapis.com/css2?family=Poppins:wght@400;500;600;700&display=swap">
<style>
  :root{
    --backdrop:#16171a;
    --card:#1a1e2b;
    --card-deep:#141824;
    --navy:#000a20;
    --blue:#0056a2;
    --blue-mid:#0088ce;
    --cyan:#00b5ef;
    --sky:#68cef2;
    --silver:#8a8d94;
    --ink-light:#d6d9df;
    --ink-muted:#a9adb6;
  }
  *{margin:0;padding:0;box-sizing:border-box}
  html,body{width:1200px;height:852px;overflow:hidden}
  body{
    background:var(--backdrop);
    font-family:"Poppins",sans-serif;
    position:relative;
  }
  .card{
    position:absolute;
    top:277px;
    width:520px;
    height:298px;
    border-radius:22px;
    overflow:hidden;
    background:linear-gradient(160deg,var(--card) 0%,var(--card-deep) 100%);
    box-shadow:0 14px 30px rgba(0,0,0,.55);
  }
  .card--front{left:50px}
  .card--back{left:630px}
  .card__stripe{
    position:absolute;left:0;right:0;bottom:16px;height:9px;
    background:var(--blue);
  }
  /* front */
  .front__wordmark{
    position:absolute;left:0;right:0;top:96px;
    text-align:center;
    font-weight:600;font-size:44px;letter-spacing:1px;
    color:var(--silver);
  }
  .front__url{
    position:absolute;left:0;right:0;bottom:46px;
    text-align:center;
    font-size:11px;letter-spacing:7px;
    color:var(--ink-muted);
  }
  /* back */
  .back__wordmark{
    position:absolute;left:34px;top:128px;
    font-weight:600;font-size:30px;
    color:var(--blue-mid);
  }
  .back__details{position:absolute;left:288px;top:62px}
  .back__name{
    font-weight:600;font-size:19px;color:var(--blue-mid);line-height:1.1;
  }
  .back__title{
    font-size:10px;color:var(--ink-muted);margin-bottom:22px;
  }
  .contact{
    display:flex;align-items:center;gap:10px;
    font-size:12px;color:var(--ink-light);line-height:20px;
  }
  .contact svg{width:12px;height:12px;fill:var(--sky)}
  .contact--address{padding-left:22px;margin-top:6px}
</style>
</head>
<body>
  <section class="card card--front">
    <div class="front__wordmark">RMT Property</div>
    <div class="front__url">www.rmtproperty.com</div>
    <div class="card__stripe"></div>
  </section>

  <section class="card card--back">
    <div class="back__wordmark">RMT Property</div>
    <div class="back__details">
      <div class="back__name">Callum Reid</div>
      <div class="back__title">Associate Director</div>
      <div class="contact">
        <svg viewBox="0 0 24 24" aria-hidden="true"><path d="M6.6 10.8a15.1 15.1 0 0 0 6.6 6.6l2.2-2.2a1 1 0 0 1 1-.25 11.4 11.4 0 0 0 3.6.57 1 1 0 0 1 1 1V20a1 1 0 0 1-1 1A17 17 0 0 1 3 4a1 1 0 0 1 1-1h3.5a1 1 0 0 1 1 1c0 1.25.2 2.45.57 3.57a1 1 0 0 1-.25 1z"/></svg>
        <span>555-014-2290</span>
      </div>
      <div class="contact">
        <svg viewBox="0 0 24 24" aria-hidden="true"><path d="M2 5h20v14H2zm2 2v.5l8 5 8-5V7l-8 5z"/></svg>
        <span>callum@rmtproperty.com</span>
      </div>
      <div class="contact">
        <svg viewBox="0 0 24 24" aria-hidden="true"><path d="M12 2a10 10 0 1 0 0 20 10 10 0 0 0 0-20zm6.9 6h-3a15.7 15.7 0 0 0-1.3-3.6A8 8 0 0 1 18.9 8zM12 4c.8 1.2 1.5 2.5 1.9 4h-3.8c.4-1.5 1.1-2.8 1.9-4zM4.3 14a8 8 0 0 1 0-4h3.4a16 16 0 0 0 0 4zm.8 2h3a15.7 15.7 0 0 0 1.3 3.6A8 8 0 0 1 5.1 16zm3-8h-3a8 8 0 0 1 4.3-3.6A15.7 15.7 0 0 0 8.1 8zM12 20c-.8-1.2-1.5-2.5-1.9-4h3.8c-.4 1.5-1.1 2.8-1.9 4zm2.3-6H9.7a14.6 14.6 0 0 1 0-4h4.6a14.6 14.6 0 0 1 0 4zm.3 5.6a15.7 15.7 0 0 0 1.3-3.6h3a8 8 0 0 1-4.3 3.6zm1.7-5.6a16 16 0 0 0 0-4h3.4a8 8 0 0 1 0 4z"/></svg>
        <span>www.rmtproperty.com</span>
      </div>
      <div class="contact contact--address">27 Kestrel Lane Northmead</div>
    </div>
    <div class="card__stripe"></div>
  </section>
</body>
</html>
```